Cosmetics Brand Logo and Bottle Label Design

We are creating a new cosmetics brand called "Milo Tennant" and would like you to create an amazing logo and bottle label for this brand's new 100% pure argan oil product.
For the logo, we really like the logo's of Vanra Okell and Ruvi. The text should be Sans Serif (without feet).
For the actual bottle label, please find attached labels of one of our competitors design which really like. We really like the simplicity and elegance of the design. The only difference is that our product will be using light turqoise as the brand color. Please feel free to add your own creativity into it as well.
Industry/Entity Type
Cosmetics
Logo Text
Milo Tennant
Font styles to use

```html
<!DOCTYPE html>
<html lang="en">
<head>
<meta charset="utf-8">
<title>Milo Tennant – Argan Oil Label</title>
<link href="https://fonts.googleapis.com/css2?family=Josefin+Sans:wght@300&family=Open+Sans:wght@300;400&display=swap" rel="stylesheet">
<style>
  :root {
    --paper: #ffffff;
    --ink: #1a1a1a;
    --turquoise: #82cfc5;
    --label-ink: #ffffff;
    --leaf: #8dc63f;
    --nut: #b5703f;
    --shell: #a8b54a;
  }
  * { margin: 0; padding: 0; box-sizing: border-box; }
  html, body {
    width: 1200px;
    height: 971px;
    overflow: hidden;
    background: var(--paper);
  }
  .canvas {
    position: relative;
    width: 1200px;
    height: 971px;
  }

  /* Brand wordmark */
  .wordmark {
    position: absolute;
    left: 366px;
    top: 190px;
    width: 792px;
    height: 88px;
    display: flex;
    align-items: center;
    gap: 22px;
    color: var(--ink);
  }
  .wordmark-dot {
    flex: 0 0 auto;
    width: 80px;
    height: 80px;
    border-radius: 50%;
    border: 3px solid var(--ink);
  }
  .wordmark-name {
    font-family: "Josefin Sans", "Gill Sans", sans-serif;
    font-weight: 300;
    font-size: 84px;
    line-height: 1;
    letter-spacing: 1px;
    text-transform: uppercase;
    padding-top: 10px;
    white-space: nowrap;
  }

  /* Flat bottle label */
  .label {
    position: absolute;
    left: 480px;
    top: 390px;
    width: 562px;
    height: 466px;
    background: var(--turquoise);
    color: var(--label-ink);
  }
  .label-brand {
    position: absolute;
    left: 60px;
    top: 108px;
    display: flex;
    align-items: center;
    gap: 10px;
  }
  .label-brand-dot {
    width: 44px;
    height: 44px;
    border-radius: 50%;
    border: 2px solid var(--label-ink);
  }
  .label-brand-name {
    font-family: "Josefin Sans", "Gill Sans", sans-serif;
    font-weight: 300;
    font-size: 46px;
    line-height: 1;
    text-transform: uppercase;
    padding-top: 6px;
    white-space: nowrap;
  }
  .label-product {
    position: absolute;
    left: 148px;
    top: 168px;
    font-family: "Open Sans", Arial, sans-serif;
    font-weight: 300;
    font-size: 27px;
    letter-spacing: 0.5px;
    white-space: nowrap;
  }
  .label-claim {
    position: absolute;
    left: 46px;
    top: 222px;
    width: 180px;
    transform-origin: left top;
    transform: translateX(48px) rotate(90deg);
    font-family: "Open Sans", Arial, sans-serif;
    font-weight: 400;
    font-size: 15px;
    line-height: 1.25;
  }
  .label-illustration {
    position: absolute;
    left: 138px;
    top: 222px;
    width: 318px;
    height: 138px;
    border-radius: 40px 60px 50px 70px;
    background:
      radial-gradient(ellipse at 72% 58%, var(--nut) 0%, rgba(181,112,63,0) 38%),
      radial-gradient(ellipse at 60% 50%, var(--shell) 0%, rgba(168,181,74,0) 55%),
      linear-gradient(100deg, rgba(141,198,63,0) 0%, var(--leaf) 30%, rgba(141,198,63,0.4) 60%, rgba(141,198,63,0) 100%);
  }
</style>
</head>
<body>
  <main class="canvas">
    <header class="wordmark">
      <span class="wordmark-dot" aria-hidden="true"></span>
      <span class="wordmark-name">Milo Tennant</span>
    </header>

    <section class="label">
      <div class="label-brand">
        <span class="label-brand-dot" aria-hidden="true"></span>
        <span class="label-brand-name">Milo Tennant</span>
      </div>
      <p class="label-product">100% pure argan oil</p>
      <p class="label-claim">ultra lightweight<br>moisturizing oil</p>
      <div class="label-illustration" role="img" aria-label="Argan nuts in green husks with leaves on a sprig"></div>
    </section>
  </main>
</body>
</html>
```